Business Card Design

We are a manufacturing and distribution company with most of our customer base being supermarkets. We have established brand guidelines that are attached.

```html
<!DOCTYPE html>
<html lang="en">
<head>
<meta charset="utf-8">
<title>Valorenz Business Card</title>
<link rel="stylesheet" href="https://fonts.googleapis.com/css2?family=Montserrat:wght@400;500;600;700;800&display=swap">
<style>
  :root {
    --brand-blue: #1f68b5;
    --brand-red: #e8141c;
    --ink: #111111;
    --muted: #555555;
    --card: #ffffff;
    --backdrop: #6e6e6e;
  }
  * { margin: 0; padding: 0; box-sizing: border-box; }
  html, body { width: 1200px; height: 1056px; overflow: hidden; }
  body {
    background: var(--backdrop);
    font-family: "Montserrat", sans-serif;
    display: flex;
    flex-direction: column;
    align-items: center;
    justify-content: center;
    gap: 80px;
  }
  .card {
    width: 600px;
    height: 343px;
    background: var(--card);
    position: relative;
    overflow: hidden;
  }
  /* Front */
  .card-front { display: flex; }
  .accent-panel {
    width: 250px;
    height: 100%;
    display: flex;
  }
  .accent-stripe { width: 34px; background: var(--brand-red); }
  .accent-gap { width: 14px; background: var(--card); }
  .accent-block { flex: 1; background: var(--brand-blue); }
  .details {
    flex: 1;
    padding: 46px 40px 36px 20px;
    display: flex;
    flex-direction: column;
    align-items: flex-end;
    text-align: right;
  }
  .brand {
    display: flex;
    align-items: center;
    gap: 10px;
    font-weight: 800;
    color: var(--ink);
    letter-spacing: 0.04em;
  }
  .brand-mark { width: 14px; height: 14px; background: var(--brand-blue); }
  .details .brand { font-size: 30px; }
  .person { margin-top: 26px; }
  .person-name {
    font-size: 22px;
    color: var(--brand-blue);
    letter-spacing: 0.02em;
  }
  .person-name .first { font-weight: 700; }
  .person-name .last { font-weight: 500; }
  .person-role {
    font-size: 14px;
    font-weight: 600;
    color: var(--brand-red);
    margin-top: 2px;
  }
  .contacts {
    list-style: none;
    margin-top: auto;
    display: flex;
    flex-direction: column;
    gap: 7px;
  }
  .contacts li {
    display: flex;
    align-items: center;
    justify-content: flex-end;
    gap: 8px;
    font-size: 12px;
    color: var(--muted);
  }
  .contact-icon {
    width: 17px;
    height: 17px;
    background: var(--ink);
    border-radius: 3px;
    display: flex;
    align-items: center;
    justify-content: center;
  }
  .contact-icon svg { width: 11px; height: 11px; }
  /* Back */
  .card-back {
    display: flex;
    align-items: center;
    justify-content: center;
  }
  .card-back .brand { font-size: 48px; gap: 16px; }
  .card-back .brand-mark { width: 22px; height: 22px; }
</style>
</head>
<body>
  <section class="card card-front">
    <div class="accent-panel">
      <div class="accent-stripe"></div>
      <div class="accent-gap"></div>
      <div class="accent-block"></div>
    </div>
    <div class="details">
      <div class="brand"><span class="brand-mark"></span>VALORENZ</div>
      <div class="person">
        <div class="person-name"><span class="first">MARA</span> <span class="last">QUILL</span></div>
        <div class="person-role">Manager</div>
      </div>
      <ul class="contacts">
        <li>(555) 014-2738
          <span class="contact-icon"><svg viewBox="0 0 12 12"><path d="M3 1 L4.6 3.4 L3.6 4.6 Q4.6 6.8 7.4 8.4 L8.6 7.4 L11 9 L10 11 Q5.5 11 1 3 Z" fill="#fff"/></svg></span>
        </li>
        <li>info@valorenzmail.com
          <span class="contact-icon"><svg viewBox="0 0 12 12"><rect x="1" y="2.5" width="10" height="7" fill="none" stroke="#fff" stroke-width="1.2"/><path d="M1 2.5 L6 7 L11 2.5" fill="none" stroke="#fff" stroke-width="1.2"/></svg></span>
        </li>
        <li>www.valorenz.com
          <span class="contact-icon"><svg viewBox="0 0 12 12"><path d="M3 1 L3 10 L5.2 8 L6.8 11 L8.2 10.3 L6.7 7.4 L9.5 7.2 Z" fill="#fff"/></svg></span>
        </li>
      </ul>
    </div>
  </section>

  <section class="card card-back">
    <div class="brand"><span class="brand-mark"></span>VALORENZ</div>
  </section>
</body>
</html>
```